UI/ UX Design for ERP Software

We need a new UX/UI interface for a ERP software for property managers. Our CMMS / ERP solution is made based on responsive design technologies and is coded in PHP.
The overall UX to be similar to Zel Kavo - easy navigation, intuitive menus.

Industry/Entity Type

Property Management

Number of Pages Required

5+ page

Requirements
Must have
• Round dock buttons
Consistent icons across the application
Enough Spacing between buttons/icons/ menu
Consistent Font
Nice to have
• We would like the UX to allow the users to use the application without /minimum training.
Should not have
• we don't want anything that is classic with respect to UX

```html
<!DOCTYPE html>
<html lang="en">
<head>
<meta charset="utf-8">
<title>Quelvo – Property ERP Screens</title>
<link href="https://fonts.googleapis.com/css2?family=Poppins:wght@400;500;600;700&display=swap" rel="stylesheet">
<style>
:root{
  --page:#b9b8c8;
  --blue:#0b7ff5;
  --blue-2:#18acf8;
  --ink:#2f3b55;
  --ink-soft:#4c5670;
  --muted:#9aa1b3;
  --line:#e6e9f0;
  --panel:#ffffff;
  --canvas:#f4f5f9;
  --pill:#eceef3;
  --green:#8bc34a;
  --sky:#06a9f4;
  --orange:#ee9d3e;
  --coral:#f77d7d;
  --stripe:#f3f5f9;
}
*{box-sizing:border-box;margin:0;padding:0}
html,body{width:1200px;height:2396px;overflow:hidden;background:var(--page)}
body{font-family:'Poppins',sans-serif;color:var(--ink)}
.stage{position:absolute;left:0;top:0;width:1290px;height:2576px;transform:scale(.93023);transform-origin:0 0}
.screen{position:absolute;width:997px;height:665px;background:var(--canvas);overflow:hidden;box-shadow:0 30px 50px rgba(60,60,90,.25)}
.abs{position:absolute}
.topbar{position:absolute;top:0;height:53px;background:linear-gradient(90deg,var(--blue),var(--blue-2));color:#fff}
.search{position:absolute;top:18px;font-size:13px;color:rgba(255,255,255,.85);display:flex;align-items:center;gap:8px}
.gear{position:absolute;top:11px;width:31px;height:31px;border-radius:50%;background:rgba(255,255,255,.22);display:flex;align-items:center;justify-content:center}
.avatar{position:absolute;top:12px;width:29px;height:29px;border-radius:50%;background:linear-gradient(#6d7a90,#3b4458)}
.user{position:absolute;top:14px;line-height:1}
.user b{display:block;font-size:12.5px;font-weight:600}
.user small{font-size:7.5px}
.chev{position:absolute;top:22px}
.brand{display:flex;align-items:center;gap:6px;font-weight:600;font-size:22px}
.brand i{width:14px;height:14px;border-radius:3px;display:block}

/* screen 1 */
.sidebar{position:absolute;left:0;top:0;width:208px;height:665px;background:#fff}
.sidebar .brand{position:absolute;left:36px;top:26px;color:var(--blue)}
.sidebar .brand i{background:var(--blue)}
.nav{position:absolute;left:20px;top:92px;list-style:none}
.nav li{height:44.3px;display:flex;align-items:center;gap:9px;font-size:11.5px;font-weight:500;color:var(--ink-soft)}
.nav li.on{font-weight:600;font-size:13px;color:var(--ink)}
.nav svg{width:17px;height:17px;fill:none;stroke:var(--ink-soft);stroke-width:1.4}
.nav li.on svg{stroke:var(--blue)}
.h1{position:absolute;font-size:23px;font-weight:600;color:var(--ink-soft)}
.stat{position:absolute;top:146px;width:140px;height:119px;background:#fff;border-radius:4px}
.stat svg{position:absolute;right:18px;top:12px;width:40px;height:40px;fill:none;stroke:var(--blue);stroke-width:1.3}
.stat span{position:absolute;left:12px;top:69px;font-size:9.5px;color:var(--muted)}
.stat b{position:absolute;left:12px;top:83px;font-size:13px;font-weight:600;color:var(--ink)}
.chart{position:absolute;left:237px;top:285px;width:730px;height:311px;background:#fff;border-radius:4px}
.range{position:absolute;left:18px;top:28px;font-size:10px;display:flex;gap:6px;align-items:center;color:var(--ink-soft)}
.pills{position:absolute;left:188px;top:25px;display:flex;gap:8px}
.pills span{background:var(--pill);border-radius:10px;font-size:9px;padding:4px 10px;color:var(--ink-soft);font-weight:500}
.legend{position:absolute;left:56px;top:260px;display:grid;grid-template-columns:143px 197px 176px auto;row-gap:3px;font-size:8.5px;color:var(--ink-soft)}
.legend span::before{content:"";display:inline-block;width:5px;height:5px;border-radius:50%;background:var(--c);margin-right:5px;vertical-align:1px}
.copy{position:absolute;left:208px;right:0;top:635px;text-align:center;font-size:11.5px;color:var(--ink-soft);font-weight:500}

/* screen 2 & 3 header */
.wide{left:0;width:997px;height:52px}
.wide .brand{position:absolute;left:30px;top:12px;color:#fff}
.wide .brand i{background:#fff}
.h2{position:absolute;font-size:15px;font-weight:600;color:var(--ink-soft)}
.card{position:absolute;background:#fff;border-radius:4px}
.thumbs{position:absolute;left:27px;top:27px;display:flex;gap:7px}
.thumbs figure{width:54px;text-align:center;font-size:8px;color:var(--muted)}
.thumbs .ph{height:47px;border-radius:2px;margin-bottom:7px;background:linear-gradient(#6f9fcc,#a79c8e)}
.cap{position:absolute;left:18px;font-size:7.8px;font-weight:600;color:var(--ink-soft)}
.mini{position:absolute;left:18px;width:261px;border:1px solid #dcdfe7;border-radius:3px;border-collapse:collapse;font-size:7px;font-weight:600;color:var(--ink-soft)}
.mini td{border:1px solid #e3e6ec;height:19px;padding:0 6px}
.mini tr:first-child td{height:27px}
.cal-title{position:absolute;left:24px;top:22px;font-size:16px;font-weight:500;color:var(--ink-soft)}
.tabs{position:absolute;left:237px;top:24px;display:flex;gap:5px}
.tabs span{background:var(--pill);border-radius:10px;font-size:10px;padding:2px 11px;color:var(--muted)}
.tabs .on{background:#e8f4fe;color:var(--sky)}
.today{position:absolute;right:22px;top:18px;display:flex;gap:5px;align-items:center;font-size:9.5px;color:var(--muted)}
.today i{width:27px;height:27px;border:1px solid var(--line);border-radius:50%;display:flex;align-items:center;justify-content:center;font-style:normal;font-size:12px}
.cal-rule{position:absolute;left:22px;right:22px;top:62px;border-top:1px solid var(--line)}
.days{position:absolute;left:2px;right:0;top:82px;display:grid;grid-template-columns:repeat(7,1fr);font-size:11px;font-weight:600;color:var(--ink-soft);text-align:center}
.grid{position:absolute;left:2px;right:0;top:115px;display:grid;grid-template-columns:repeat(7,1fr);grid-auto-rows:74px;border-top:1px solid var(--line)}
.grid div{border-right:1px solid var(--line);border-bottom:1px solid var(--line);font-size:12px;color:var(--muted);text-align:right;padding:12px 14px 0 8px;position:relative}
.grid div:nth-child(7n){border-right:0}
.grid .ev{color:#fff;font-weight:600}
.grid .ev p{position:absolute;left:8px;bottom:10px;text-align:left;font-size:8.5px;line-height:1.45}

/* screen 3 */
.subnav{position:absolute;left:0;top:53px;width:997px;height:40px;background:#fff;display:flex;justify-content:space-between;padding:0 32px 0 29px;align-items:center;font-size:10px;font-weight:500;color:var(--ink-soft);white-space:nowrap}
.subnav .on{color:var(--blue);font-weight:600;font-size:11px}
.crumb{position:absolute;right:30px;top:117px;font-size:10px;font-weight:500;color:var(--ink-soft);display:flex;gap:6px;align-items:center}
.edit{position:absolute;left:542px;top:175px;height:31px;width:124px;border-radius:16px;background:var(--blue);color:#fff;font-size:10px;font-weight:600;display:flex;align-items:center;justify-content:center;gap:5px}
.info{position:absolute;left:54px;top:224px;width:612px;border-collapse:collapse;font-size:8.8px;color:var(--ink-soft);table-layout:fixed}
.info td{height:29.5px;padding:0;white-space:nowrap;overflow:hidden}
.info tr:nth-child(even){background:var(--stripe)}
.info .k{font-weight:500;color:var(--ink);padding-left:12px;width:148px}
.info .v{width:192px}
.info .k2{font-weight:500;color:var(--ink);width:142px}
.photo{position:absolute;left:699px;width:238px;border-radius:2px}
</style>
</head>
<body>
<div class="stage">

<!-- Screen 1 : Dashboard -->
<section class="screen" style="left:147px;top:225px">
  <aside class="sidebar">
    <div class="brand"><i></i>Quelvo</div>
    <ul class="nav">
      <li class="on"><svg viewBox="0 0 16 16"><circle cx="8" cy="8" r="6.5"/><path d="M8 8l3-3"/></svg>Dashboard</li>
      <li><svg viewBox="0 0 16 16"><circle cx="6" cy="5" r="3"/><path d="M1 14c0-3 2-5 5-5s5 2 5 5M11 2a3 3 0 010 6M13 9c1 1 2 3 2 5"/></svg>Customers</li>
      <li><svg viewBox="0 0 16 16"><path d="M2 8l6-6 6 6v6H2z"/></svg>Properties</li>
      <li><svg viewBox="0 0 16 16"><path d="M2 8l6-6 6 6v6H2z"/></svg>Tenant</li>
      <li><svg viewBox="0 0 16 16"><rect x="3" y="1.5" width="11" height="13" rx="1"/><circle cx="8.5" cy="6.5" r="2"/><path d="M5.5 12c0-2 1.5-3 3-3s3 1 3 3M1.5 4h2M1.5 8h2M1.5 12h2"/></svg>Contact</li>
      <li><svg viewBox="0 0 16 16"><circle cx="8" cy="5" r="3"/><path d="M4 4h8M2 15c0-3.5 2.5-6 6-6s6 2.5 6 6z"/></svg>Contractors</li>
      <li><svg viewBox="0 0 16 16"><circle cx="6" cy="5" r="3"/><path d="M1 14c0-3 2-5 5-5s5 2 5 5M11 2a3 3 0 010 6M13 9c1 1 2 3 2 5"/></svg>Employees</li>
      <li><svg viewBox="0 0 16 16"><rect x="4" y="2" width="11" height="12" rx="2"/><circle cx="4" cy="8" r="3"/><path d="M8 6h5M8 10h5"/></svg>Compliance Manag...</li>
      <li><svg viewBox="0 0 16 16"><path d="M2 2l12 12M14 2L2 14M2 2l3 0M14 14l-3 0"/><circle cx="3" cy="13" r="1.5"/><circle cx="13" cy="3" r="1.5"/></svg>Prevent. Mainten...</li>
      <li><svg viewBox="0 0 16 16"><rect x="2" y="1.5" width="12" height="13" rx="1"/><path d="M5 5h6M5 8h6M5 11l2 1 4-4"/></svg>Work Orders</li>
      <li><svg viewBox="0 0 16 16"><path d="M1 3h2l2 8h8l2-6H4"/><circle cx="6" cy="14" r="1"/><circle cx="12" cy="14" r="1"/><path d="M6 1h6M9 1v4"/></svg>Purchase Orders</li>
      <li><svg viewBox="0 0 16 16"><path d="M2 8l6-6 6 6v6H2z"/></svg>Property Inspections</li>
    </ul>
  </aside>
  <header class="topbar" style="left:208px;width:789px">
    <div class="search" style="left:22px"><svg width="13" height="13" viewBox="0 0 14 14" fill="none" stroke="#fff" stroke-width="1.6"><circle cx="6" cy="6" r="4.5"/><path d="M9.5 9.5L13 13"/></svg>Search...</div>
    <div class="gear" style="left:595px"><svg width="15" height="15" viewBox="0 0 16 16" fill="#fff"><path d="M7 0h2l.4 2.2 1.6.7 1.9-1.3 1.4 1.4-1.3 1.9.7 1.6L16 7v2l-2.2.4-.7 1.6 1.3 1.9-1.4 1.4-1.9-1.3-1.6.7L9 16H7l-.4-2.2-1.6-.7-1.9 1.3-1.4-1.4 1.3-1.9-.7-1.6L0 9V7l2.2-.4.7-1.6-1.3-1.9 1.4-1.4 1.9 1.3 1.6-.7z"/><circle cx="8" cy="8" r="2.6" fill="#2a95f7"/></svg></div>
    <div class="avatar" style="left:636px"></div>
    <div class="user" style="left:673px"><b>Dana Reyes</b><small>CEO founder</small></div>
    <svg class="chev" style="left:760px" width="9" height="6" viewBox="0 0 9 6" fill="none" stroke="#fff" stroke-width="1.4"><path d="M1 1l3.5 3.5L8 1"/></svg>
  </header>

  <h1 class="h1" style="left:238px;top:104px">Active Dashboard</h1>

  <div class="stat" style="left:237px"><svg viewBox="0 0 40 40"><rect x="4" y="14" width="14" height="22"/><rect x="18" y="4" width="16" height="32"/><path d="M7 19h3v3H7zM12 19h3v3h-3zM7 26h3v3H7zM12 26h3v3h-3zM22 9h3v3h-3zM28 9h3v3h-3zM22 16h3v3h-3zM28 16h3v3h-3zM22 23h3v3h-3zM28 23h3v3h-3z"/></svg><span>Properties</span><b>3 homes</b></div>
  <div class="stat" style="left:385px"><svg viewBox="0 0 40 40"><rect x="6" y="3" width="20" height="30"/><path d="M10 8h12M10 13h12M10 18h6"/><circle cx="27" cy="24" r="5"/><path d="M19 38c0-5 4-8 8-8s8 3 8 8"/></svg><span>Tenants</span><b>8 Tenants</b></div>
  <div class="stat" style="left:533px"><svg viewBox="0 0 40 40"><rect x="6" y="12" width="22" height="22"/><path d="M6 5h22M9 2l-3 3 3 3M25 2l3 3-3 3M35 12v22M32 15l3-3 3 3M32 31l3 3 3-3"/></svg><span>Properties Area</span><b>422,000.00 sq.ft</b></div>
  <div class="stat" style="left:681px"><svg viewBox="0 0 40 40"><path d="M3 18L20 4l17 14M7 15v20h26V15"/><rect x="10" y="20" width="20" height="8"/><circle cx="20" cy="12" r="2"/></svg><span>Rented Area</span><b>233,500.00 sq.ft</b></div>
  <div class="stat" style="left:829px"><svg viewBox="0 0 40 40"><circle cx="17" cy="16" r="11"/><path d="M25 24l11 11M12 13h10M12 17h10M12 21h6"/></svg><span>Vacancies Area</span><b>188,500.00 sq.ft</b></div>

  <div class="chart">
    <div class="range"><svg width="12" height="12" viewBox="0 0 12 12" fill="none" stroke="#4c5670" stroke-width="1.2"><rect x="1" y="2" width="10" height="9"/><path d="M1 5h10M4 1v2M8 1v2"/></svg>12-27-2021 - 01-03-2021</div>
    <div class="pills"><span>Last 7 days</span><span>Last months</span><span>Last 3 months</span><span>Next 7 days</span><span>Next months</span><span>Next 3 months</span></div>
    <svg class="abs" style="left:0;top:0" width="730" height="250" viewBox="0 0 730 250" font-family="Poppins, sans-serif" font-size="6" fill="#8a92a6">
      <defs><linearGradient id="areaFill" x1="0" y1="0" x2="0" y2="1"><stop offset="0" stop-color="#0b7ff5" stop-opacity=".28"/><stop offset="1" stop-color="#0b7ff5" stop-opacity=".03"/></linearGradient></defs>
      <g stroke="#edf0f5"><path d="M40 82H700M40 111H700M40 140H700M40 169H700M40 199H700M40 231H700"/></g>
      <text x="18" y="84">10K</text><text x="18" y="113">08K</text><text x="18" y="142">06K</text><text x="18" y="171">04K</text><text x="18" y="201">02K</text><text x="26" y="233">0</text>
      <path d="M38 142C44 136 48 134 52 132S76 118 86 114C120 100 150 98 173 102C210 108 240 128 264 141C300 164 320 190 342 194C372 200 384 156 406 153C436 150 458 178 483 180C512 182 530 150 551 132C570 112 588 92 607 82C640 58 680 74 695 99L695 231L38 231Z" fill="url(#areaFill)"/>
      <path d="M38 142C44 136 48 134 52 132S76 118 86 114C120 100 150 98 173 102C210 108 240 128 264 141C300 164 320 190 342 194C372 200 384 156 406 153C436 150 458 178 483 180C512 182 530 150 551 132C570 112 588 92 607 82C640 58 680 74 695 99" fill="none" stroke="#0b8af7" stroke-width="1.8"/>
      <g fill="#0b8af7" stroke="#fff" stroke-width="1"><circle cx="52" cy="132" r="3"/><circle cx="86" cy="114" r="3"/><circle cx="173" cy="102" r="3"/><circle cx="264" cy="141" r="3"/><circle cx="342" cy="194" r="3"/><circle cx="406" cy="153" r="3"/><circle cx="483" cy="180" r="3"/><circle cx="551" cy="132" r="3"/><circle cx="607" cy="82" r="3"/><circle cx="695" cy="99" r="3"/></g>
      <g text-anchor="middle">
        <text x="52" y="240">01</text><text x="73.5" y="240">02</text><text x="95" y="240">03</text><text x="116.5" y="240">04</text><text x="138" y="240">05</text><text x="159.5" y="240">06</text><text x="181" y="240">07</text><text x="202.5" y="240">08</text><text x="224" y="240">09</text><text x="245.5" y="240">10</text><text x="267" y="240">11</text><text x="288.5" y="240">12</text><text x="310" y="240">13</text><text x="331.5" y="240">14</text><text x="353" y="240">15</text><text x="374.5" y="240">16</text><text x="396" y="240">17</text><text x="417.5" y="240">18</text><text x="439" y="240">19</text><text x="460.5" y="240">20</text><text x="482" y="240">21</text><text x="503.5" y="240">22</text><text x="525" y="240">23</text><text x="546.5" y="240">24</text><text x="568" y="240">25</text><text x="589.5" y="240">26</text><text x="611" y="240">27</text><text x="632.5" y="240">28</text><text x="654" y="240">29</text><text x="675.5" y="240">30</text><text x="697" y="240">31</text>
      </g>
    </svg>
    <div class="legend">
      <span style="--c:#3fb2f5">Scheduled Maintenance</span><span style="--c:#8bc34a">Completed Scheduled Maintenance</span><span style="--c:#ff8c5a">Future Scheduled Maintenance</span><span style="--c:#f5558a">Scheduled Work Orders</span>
      <span style="--c:#8a9bb4">Completed Work Orders</span><span style="--c:#f5c542">Property Inspections In Progress</span><span style="--c:#9b6cf5">Completed Property Inspections</span>
    </div>
  </div>
  <p class="copy">© Copyrights Quelvo 2021</p>
</section>

<!-- Screen 2 : Assigned properties & calendar -->
<section class="screen" style="left:145px;top:956px">
  <header class="topbar wide">
    <div class="brand"><i></i>Quelvo</div>
    <div class="search" style="left:231px"><svg width="13" height="13" viewBox="0 0 14 14" fill="none" stroke="#fff" stroke-width="1.6"><circle cx="6" cy="6" r="4.5"/><path d="M9.5 9.5L13 13"/></svg>Search...</div>
    <div class="gear" style="left:803px"><svg width="15" height="15" viewBox="0 0 16 16" fill="#fff"><path d="M7 0h2l.4 2.2 1.6.7 1.9-1.3 1.4 1.4-1.3 1.9.7 1.6L16 7v2l-2.2.4-.7 1.6 1.3 1.9-1.4 1.4-1.9-1.3-1.6.7L9 16H7l-.4-2.2-1.6-.7-1.9 1.3-1.4-1.4 1.3-1.9-.7-1.6L0 9V7l2.2-.4.7-1.6-1.3-1.9 1.4-1.4 1.9 1.3 1.6-.7z"/><circle cx="8" cy="8" r="2.6" fill="#2a95f7"/></svg></div>
    <div class="avatar" style="left:844px"></div>
    <div class="user" style="left:881px"><b>Dana Reyes</b><small>CEO founder</small></div>
    <svg class="chev" style="left:966px" width="9" height="6" viewBox="0 0 9 6" fill="none" stroke="#fff" stroke-width="1.4"><path d="M1 1l3.5 3.5L8 1"/></svg>
  </header>

  <h2 class="h2" style="left:29px;top:90px">Assigned properties</h2>
  <h2 class="h2" style="left:331px;top:90px">Maintenance and wo calendar</h2>

  <div class="card" style="left:29px;top:123px;width:291px;height:560px">
    <div class="thumbs">
      <figure><div class="ph" role="img" aria-label="Photo of a modern two-storey house at dusk"></div>Property 1</figure>
      <figure><div class="ph" role="img" aria-label="Photo of a beige villa with balconies" style="background:linear-gradient(#8fb6dd,#c9b79c)"></div>Property 2</figure>
      <figure><div class="ph" role="img" aria-label="Photo of a white contemporary house with red accents" style="background:linear-gradient(#7fb3e6,#d7d3cf)"></div>Property 3</figure>
      <figure><div class="ph" role="img" aria-label="Photo of a grey modern residence" style="background:linear-gradient(#a8c0d6,#6b6c70)"></div>Property 4</figure>
    </div>
    <p class="cap" style="top:111px">OPEN &nbsp;TENANT REQUESTS ASSIGNED TO USER 3 REQUETS</p>
    <table class="mini" style="top:128px"><tr><td>Ticket ID</td><td>Subject</td><td>Property</td><td>Tenant</td></tr><tr><td></td><td></td><td></td><td></td></tr><tr><td></td><td></td><td></td><td></td></tr></table>
    <p class="cap" style="top:213px">OPEN MAINTENANCE ASSIGNED TO USER - 5 TICKETS</p>
    <table class="mini" style="top:231px"><tr><td></td><td style="text-align:center">ID</td><td>Property</td><td>Template</td><td>Date</td></tr><tr><td></td><td></td><td></td><td></td><td></td></tr><tr><td></td><td></td><td></td><td></td><td></td></tr></table>
    <p class="cap" style="top:316px">OPEN WO ASSIGNED TO USER - 3</p>
    <table class="mini" style="top:334px"><tr><td>Wo Name</td><td>Property</td><td>Date</td><td style="width:100px">Status</td></tr><tr><td></td><td></td><td></td><td></td></tr><tr><td></td><td></td><td></td><td></td></tr></table>
    <p class="cap" style="top:417px">PURCHASE ORDERS STATUS (LAST 5)</p>
    <table class="mini" style="top:435px"><tr><td style="text-align:center">Po</td><td>Property</td><td style="text-align:center">Cost</td><td>Created</td><td>Approved</td></tr><tr><td></td><td></td><td></td><td></td><td></td></tr><tr><td></td><td></td><td></td><td></td><td></td></tr></table>
  </div>

  <div class="card" style="left:331px;top:122px;width:636px;height:560px">
    <p class="cal-title">Calendar</p>
    <div class="tabs"><span class="on">Month</span><span>Week</span><span>Day</span></div>
    <div class="today"><i>←</i>TODAY<i>→</i></div>
    <div class="cal-rule"></div>
    <div class="days"><span>SUN</span><span>MON</span><span>TUE</span><span>WED</span><span>THU</span><span>FRI</span><span>SAT</span></div>
    <div class="grid">
      <div>1</div><div>2</div><div>3</div><div>4</div><div>5</div><div>6</div><div>7</div>
      <div>8</div><div>9</div><div>10</div><div class="ev" style="background:var(--green)">11<p># Marlow<br>court Keypad</p></div><div>12</div><div>13</div><div>14</div>
      <div>15</div><div class="ev" style="background:var(--sky)">16<p>#1106 cook<br>daily inspection</p></div><div>17</div><div>18</div><div>19</div><div class="ev" style="background:var(--orange)">20<p>#1106 cook<br>daily inspection</p></div><div>21</div>
      <div>22</div><div>23</div><div>24</div><div class="ev" style="background:var(--coral)">25<p>#1106 cook<br>daily inspection</p></div><div>26</div><div>27</div><div>28</div>
      <div>29</div><div>30</div><div>31</div><div>1</div><div>2</div><div>3</div><div>4</div>
      <div>5</div><div>6</div><div>7</div><div>8</div><div>9</div><div>10</div><div>11</div>
    </div>
  </div>
</section>

<!-- Screen 3 : Property detail -->
<section class="screen" style="left:146px;top:1686px">
  <header class="topbar wide">
    <div class="brand"><i></i>Quelvo</div>
    <div class="search" style="left:231px"><svg width="13" height="13" viewBox="0 0 14 14" fill="none" stroke="#fff" stroke-width="1.6"><circle cx="6" cy="6" r="4.5"/><path d="M9.5 9.5L13 13"/></svg>Search...</div>
    <div class="gear" style="left:803px"><svg width="15" height="15" viewBox="0 0 16 16" fill="#fff"><path d="M7 0h2l.4 2.2 1.6.7 1.9-1.3 1.4 1.4-1.3 1.9.7 1.6L16 7v2l-2.2.4-.7 1.6 1.3 1.9-1.4 1.4-1.9-1.3-1.6.7L9 16H7l-.4-2.2-1.6-.7-1.9 1.3-1.4-1.4 1.3-1.9-.7-1.6L0 9V7l2.2-.4.7-1.6-1.3-1.9 1.4-1.4 1.9 1.3 1.6-.7z"/><circle cx="8" cy="8" r="2.6" fill="#2a95f7"/></svg></div>
    <div class="avatar" style="left:844px"></div>
    <div class="user" style="left:881px"><b>Dana Reyes</b><small>CEO founder</small></div>
    <svg class="chev" style="left:966px" width="9" height="6" viewBox="0 0 9 6" fill="none" stroke="#fff" stroke-width="1.4"><path d="M1 1l3.5 3.5L8 1"/></svg>
  </header>
  <nav class="subnav"><span class="on">General Info</span><span>Organization Chart</span><span>Tenant List</span><span>Property Assets</span><span>Contractors List</span><span>Compliance Manag...</span><span>Maint. Work Orders</span><span>Work Orders</span><span>Purchase Orders</span><span>Files</span></nav>
  <h1 class="h1" style="left:27px;top:106px;font-size:22px">Prime Tower</h1>
  <div class="crumb"><svg width="12" height="11" viewBox="0 0 12 11" fill="#4c5670"><path d="M6 0l6 5h-2v6H7.5V7.5h-3V11H2V5H0z"/></svg>HOME <span>/</span> PROPERTIES</div>

  <div class="card" style="left:29px;top:155px;width:938px;height:560px"></div>
  <h2 class="h2" style="left:54px;top:181px">General Information</h2>
  <div class="edit"><svg width="11" height="11" viewBox="0 0 12 12" fill="none" stroke="#fff" stroke-width="1.3"><path d="M6 1H1v10h10V6M5 7l.5-2L10 .5l1.5 1.5L7 6.5z"/></svg>PROPERTY EDIT</div>
  <h2 class="h2" style="left:697px;top:179px">General Information</h2>

  <table class="info">
    <tr><td class="k">PROVINCE:</td><td class="v">British Columbia</td><td class="k2">PROVINCE:</td><td>British Columbia</td></tr>
    <tr><td class="k">CITY:</td><td class="v">Ashby Vale</td><td class="k2">CITY:</td><td>Ashby Vale</td></tr>
    <tr><td class="k">ADDRESS:</td><td class="v">12 Harbor Lane, Lakeside, BC</td><td class="k2">ADDRESS:</td><td>12 Harbor</td></tr>
    <tr><td class="k">GPS ADDRESS:</td><td class="v">50.1234567 : -120-45678900000001</td><td class="k2">GPS ADDRESS:</td><td>50.1234567 : A1B 2C3</td></tr>
    <tr><td class="k">POSTAL CODE:</td><td class="v">A1B 2C3</td><td class="k2">POSTAL CODE:</td><td>07/01/1980</td></tr>
    <tr><td class="k">DATE BUILT:</td><td class="v">07/01/1980</td><td class="k2">DATE BUILT:</td><td>150000.00</td></tr>
    <tr><td class="k">AREA (SQ.FT):</td><td class="v">150000.00</td><td class="k2">AREA (SQ.FT):</td><td></td></tr>
    <tr><td class="k">LOT SIZE:</td><td class="v"></td><td class="k2">LOT SIZE:</td><td>CDI</td></tr>
    <tr><td class="k">ZONING:</td><td class="v">CDI</td><td class="k2">ZONING:</td><td>Seel and concrete</td></tr>
    <tr><td class="k">STRUCTURE TYPE:</td><td class="v">Seel and concrete</td><td class="k2">STRUCTURE TYPE:</td><td>250</td></tr>
    <tr><td class="k">BUILDING HEIGHT:</td><td class="v">250</td><td class="k2">BUILDING HEIGHT:</td><td></td></tr>
    <tr><td class="k">CLEAR HEIGHT:</td><td class="v"></td><td class="k2">CLEAR HEIGHT:</td><td>50</td></tr>
    <tr><td class="k">FLOOR LOADING CAPACITY:</td><td class="v">50</td><td class="k2">FLOOR LOADING CAPACITY:</td><td>30</td></tr>
    <tr><td class="k">NUMBER OF FLOORS:</td><td class="v">30</td><td class="k2">NUMBER OF FLOORS:</td><td>150</td></tr>
    <tr><td class="k">SUITES</td><td class="v">150</td><td class="k2">SUITES</td><td></td></tr>
  </table>

  <div class="photo" role="img" aria-label="Photo of a modern three-storey house with stone and wood facade" style="top:221px;height:177px;background:linear-gradient(#bcd3ee,#7d7e86 60%,#5d7a4e)"></div>
  <div class="photo" role="img" aria-label="Photo of a contemporary grey and white family home" style="top:406px;height:177px;background:linear-gradient(#cfe0f2,#a9a7a1 55%,#6f7f6a)"></div>
  <div class="photo" role="img" aria-label="Photo of a white house against a blue sky" style="top:591px;height:80px;background:linear-gradient(#2d6fb8,#8fb8e0)"></div>
</section>

</div>
</body>
</html>
```